Label Design for a New Alcoholized Root Beer

Create a design for a new alcoholized root beer. This is a new product category in the USA growing very rapidly. Root Beer is a popular flavor of Cola, but recently, beer manufacturers have added alcohol to it and have created a new product that has gained traction on the market at a tremendous rate.

Root Beer is vintage product that has been around for a hundred years. Consumers of this product are mostly male between the age of 30 to 45. They purchase this product for its nostalgia and vintage look and taste.

This product will be in a standard 355 mL brown bottle.

It is 5.9% abv.

The name of the product is ''Corvel's Hard Root Beer''.

We have uploaded some pictures of traditional root beers to give you an idea of the feel we want our product to have and also, the bottle the product will be filled in.

Target Market(s)

Consumers are male 30-45, same market as craft beer consumers

Industry/Entity Type

Product

Requirements
Must have
• Design must have a vintage feel to it

```html
<!DOCTYPE html>
<html lang="en">
<head>
<meta charset="utf-8">
<title>Corvel's Hard Root Beer – Label</title>
<link rel="stylesheet" href="https://fonts.googleapis.com/css2?family=Lobster&family=Oswald:wght@700&family=Roboto+Condensed:wght@700&display=swap">
<style>
  :root {
    --page: #ffffff;
    --label-red: #b3261e;
    --label-red-dark: #7c1713;
    --panel-gold: #f4b93c;
    --panel-orange: #de7a22;
    --ink: #1c1410;
    --cream: #ffffff;
    --ring-red: #c0281f;
    --illustration-warm: #e9a24a;
    --illustration-deep: #8a4a1e;
    --hop-dark: #2a1a10;
    --wheat: #c98d24;
  }
  html, body {
    margin: 0;
    width: 1000px;
    height: 1200px;
    overflow: hidden;
    background: var(--page);
  }
  .canvas {
    position: relative;
    width: 1000px;
    height: 1200px;
  }
  .label {
    position: absolute;
    left: 180px;
    top: 110px;
    width: 640px;
    height: 980px;
  }
  .product-type {
    font-family: "Lobster", cursive;
    font-size: 100px;
    fill: var(--ink);
    stroke: var(--cream);
    stroke-width: 10px;
    paint-order: stroke fill;
    stroke-linejoin: round;
  }
  .brand-arc {
    font-family: "Oswald", sans-serif;
    font-weight: 700;
    font-size: 44px;
    letter-spacing: 2px;
    fill: var(--cream);
    stroke: var(--ink);
    stroke-width: 6px;
    paint-order: stroke fill;
    stroke-linejoin: round;
  }
  .brand-mark {
    font-family: "Oswald", sans-serif;
    font-weight: 700;
    font-size: 22px;
    fill: var(--cream);
  }
  .spec {
    font-family: "Roboto Condensed", sans-serif;
    font-weight: 700;
    font-size: 34px;
    fill: var(--ink);
  }
</style>
</head>
<body>
<main class="canvas">
  <svg class="label" viewBox="0 0 640 980" xmlns="http://www.w3.org/2000/svg" aria-label="Corvel's Hard Root Beer bottle label">
    <defs>
      <linearGradient id="label-band" x1="0" x2="1" y1="0" y2="0">
        <stop offset="0" stop-color="var(--label-red-dark)"/>
        <stop offset="0.5" stop-color="var(--label-red)"/>
        <stop offset="1" stop-color="var(--label-red-dark)"/>
      </linearGradient>
      <linearGradient id="panel-fill" x1="0" x2="1" y1="0" y2="0">
        <stop offset="0" stop-color="var(--panel-orange)"/>
        <stop offset="0.5" stop-color="var(--panel-gold)"/>
        <stop offset="1" stop-color="var(--panel-orange)"/>
      </linearGradient>
      <radialGradient id="portrait-fill" cx="0.5" cy="0.45" r="0.6">
        <stop offset="0" stop-color="var(--illustration-warm)"/>
        <stop offset="1" stop-color="var(--illustration-deep)"/>
      </radialGradient>
      <path id="brand-curve" d="M 186 500 A 134 134 0 0 1 454 500"/>
    </defs>

    <rect class="label-band" x="0" y="0" width="640" height="980" fill="url(#label-band)"/>

    <rect class="label-panel" x="44" y="44" width="552" height="891" rx="76" fill="url(#panel-fill)" stroke="var(--cream)" stroke-width="5"/>
    <rect class="label-panel-edge" x="56" y="56" width="528" height="867" rx="66" fill="none" stroke="var(--label-red)" stroke-width="6"/>

    <text class="product-type" x="320" y="226" text-anchor="middle">Root Beer</text>

    <g class="emblem">
      <g role="img" aria-label="Wreath of golden wheat ears around the emblem">
        <path d="M 122 469 A 200 200 0 0 0 268 693" fill="none" stroke="var(--wheat)" stroke-width="22" stroke-linecap="round"/>
        <path d="M 518 469 A 200 200 0 0 1 372 693" fill="none" stroke="var(--wheat)" stroke-width="22" stroke-linecap="round"/>
      </g>
      <circle cx="320" cy="500" r="180" fill="var(--ring-red)" stroke="var(--ink)" stroke-width="6"/>
      <circle cx="320" cy="500" r="118" fill="url(#portrait-fill)" stroke="var(--ink)" stroke-width="6" role="img" aria-label="Vintage illustration of a gentleman in a feathered hat raising a frothy mug, with a sunburst behind him"/>
      <text class="brand-arc">
        <textPath href="#brand-curve" startOffset="50%" text-anchor="middle">CORVEL'S HARD</textPath>
      </text>
      <g class="brand-badge">
        <circle cx="320" cy="680" r="44" fill="var(--label-red)" stroke="var(--cream)" stroke-width="4"/>
        <text class="brand-mark" x="320" y="688" text-anchor="middle">Corvel's</text>
      </g>
    </g>

    <g class="hops" role="img" aria-label="Pair of dark hop cone ornaments">
      <ellipse cx="165" cy="775" rx="55" ry="62" fill="var(--hop-dark)"/>
      <ellipse cx="470" cy="775" rx="55" ry="62" fill="var(--hop-dark)"/>
    </g>

    <text class="spec" x="230" y="904" text-anchor="middle">5.9% abv.</text>
    <text class="spec" x="422" y="904" text-anchor="middle">355 mL</text>
  </svg>
</main>
</body>
</html>
```